Stationery Design Project

Letterhead with logo and address
Envelopes with Logo and address

The target market is start-ups and
small to medium businesses primarly located in China, with less than 20
employees. Please have designers use Yellow and Blue colors and our logo
attached. Looking fr the same format as the business card attached.
Updates

Reason: Designer has been delayed working on web design

Target Market(s)

Start-ups and small to medium size businesses

Industry/Entity Type

Business

Font styles to use
Sans Serif

Requirements
Must have
Nice to have
Should not have

```html
<!DOCTYPE html>
<html lang="en">
<head>
<meta charset="utf-8">
<title>KVRM Stationery</title>
<link rel="stylesheet" href="https://fonts.googleapis.com/css2?family=Arimo:wght@400;700&display=swap">
<style>
  :root {
    --backdrop: #666666;
    --paper: #ffffff;
    --navy: #003363;
    --gold: #f2b830;
    --ink: #111111;
    --flap-line: #cfcfcf;
  }
  * { margin: 0; padding: 0; box-sizing: border-box; }
  html, body { width: 1200px; height: 824px; overflow: hidden; }
  body {
    background: var(--backdrop);
    font-family: "Arimo", Arial, sans-serif;
    position: relative;
  }
  .sheet {
    position: absolute;
    background: var(--paper);
    overflow: hidden;
  }
  .side-band {
    position: absolute;
    left: 0; top: 0; bottom: 0;
    background: var(--navy);
  }
  .brand {
    position: absolute;
    display: flex;
    flex-direction: column;
    align-items: center;
  }
  .brand-dot {
    border-radius: 50%;
    background: var(--gold);
  }
  .brand-name {
    color: #ffffff;
    font-weight: 700;
    letter-spacing: 0.18em;
  }
  .web {
    position: absolute;
    color: #ffffff;
    font-size: 7px;
    letter-spacing: 0.02em;
  }

  /* Envelope front */
  .envelope-front { left: 69px; top: 158px; width: 508px; height: 266px; }
  .envelope-front .side-band { width: 79px; }
  .envelope-front .brand { left: 0; width: 79px; top: 16px; }
  .envelope-front .brand-dot { width: 52px; height: 52px; }
  .envelope-front .brand-name { font-size: 11px; margin-top: 12px; }
  .envelope-front .web { left: 6px; bottom: 5px; }

  /* Envelope back */
  .envelope-back { left: 64px; top: 491px; width: 514px; height: 255px; }
  .envelope-back .flap { position: absolute; left: 0; top: 0; }
  .envelope-back .brand { left: 0; right: 0; top: 12px; }
  .envelope-back .brand-dot { width: 20px; height: 20px; }
  .envelope-back .brand-name { color: var(--navy); font-size: 6px; margin-top: 3px; }
  .return-address {
    position: absolute;
    left: 0; right: 0; top: 48px;
    text-align: center;
    font-size: 6.5px;
    color: var(--ink);
    letter-spacing: 0.02em;
  }

  /* Letterhead */
  .letterhead { left: 613px; top: 40px; width: 511px; height: 708px; }
  .letterhead .side-band { width: 95px; }
  .letterhead .brand { left: 0; width: 95px; top: 54px; }
  .letterhead .brand-dot { width: 66px; height: 66px; }
  .letterhead .brand-name { font-size: 13px; margin-top: 14px; }
  .letterhead .web { left: 7px; bottom: 5px; font-size: 7.5px; }
  .company-block {
    position: absolute;
    right: 18px; bottom: 4px;
    text-align: right;
    color: var(--ink);
    font-size: 7.2px;
    line-height: 10px;
  }
  .company-name { font-weight: 700; }
</style>
</head>
<body>

  <section class="sheet envelope-front">
    <div class="side-band"></div>
    <div class="brand">
      <div class="brand-dot"></div>
      <div class="brand-name">KVRM</div>
    </div>
    <div class="web">www.kvrmchina.com</div>
  </section>

  <section class="sheet envelope-back">
    <svg class="flap" width="514" height="255" viewBox="0 0 514 255" aria-hidden="true">
      <path d="M6 1 L26 52 Q30 59 40 59 L474 59 Q484 59 488 52 L508 1"
            fill="none" stroke="var(--flap-line)" stroke-width="1"/>
    </svg>
    <div class="brand">
      <div class="brand-dot"></div>
      <div class="brand-name">KVRM</div>
    </div>
    <p class="return-address">HONG QIAO LU 158, BLDG. 12, SUITE 405, SHANG HAI, SHANGHAI PROVINCE 200030 PRC</p>
  </section>

  <section class="sheet letterhead">
    <div class="side-band"></div>
    <div class="brand">
      <div class="brand-dot"></div>
      <div class="brand-name">KVRM</div>
    </div>
    <div class="web">www.kvrmchina.com</div>
    <address class="company-block" style="font-style:normal">
      <div class="company-name">KEYSTONE VENTURE AND REALTY MANAGEMENT, INC.</div>
      <div>HONG QIAO LU 158, BLDG. 12, SUITE 405</div>
      <div>SHANG HAI, SHANGHAI PROVINCE 200030 PRC</div>
    </address>
  </section>

</body>
</html>
```